women's junior contemporary apparel company.
We are looking for a business card that represents our urban design aesthetic. We would like to keep it simple and modern/contemporary.
the name of the company is 'v-lumen'.

we've attached a font style but you are not limited solely to use this font. All suggestions are welcomed.

Industry/Entity Type

Business

```html
<!DOCTYPE html>
<html lang="en">
<head>
<meta charset="utf-8">
<title>v-lumen business card</title>
<link rel="stylesheet" href="https://fonts.googleapis.com/css2?family=Oswald:wght@400;500&display=swap">
<style>
  :root {
    --page-bg: #e6e3e1;
    --card-black: #1d1c1d;
    --pattern-tone: #262526;
    --card-white: #f7f7f5;
    --ink-dark: #2b2a2a;
    --accent-red: #e5384f;
    --text-light: #e9e6e6;
    --rule-grey: #555;
  }
  * { box-sizing: border-box; margin: 0; padding: 0; }
  html, body {
    width: 1200px; height: 852px; overflow: hidden;
    background: var(--page-bg);
  }
  .stage {
    width: 1200px; height: 852px;
    display: flex; align-items: center; justify-content: center; gap: 60px;
  }
  .card {
    position: relative;
    width: 525px; height: 300px;
    box-shadow: 0 6px 18px rgba(0,0,0,0.18);
    overflow: hidden;
  }
  .brand-block {
    display: inline-flex; flex-direction: column; align-items: flex-end;
  }
  .brand-name {
    font-family: "Oswald", "Arial Narrow", sans-serif;
    font-weight: 500; line-height: 1;
  }
  .brand-tagline {
    font-family: "Oswald", "Arial Narrow", sans-serif;
    font-weight: 400; letter-spacing: 1.5px; line-height: 1;
  }

  /* Back: contact side */
  .card--back { background: var(--card-white); }
  .card--back .brand-block {
    position: absolute; left: 40px; top: 22px;
  }
  .card--back .brand-name { font-size: 46px; color: var(--ink-dark); }
  .card--back .brand-tagline {
    font-size: 10px; margin-top: 8px; color: var(--ink-dark);
  }
  .contact-fields {
    position: absolute; left: 240px; top: 118px;
    list-style: none;
    font-family: "Oswald", "Arial Narrow", sans-serif;
    font-size: 11px; line-height: 15px; letter-spacing: 0.5px;
    color: var(--ink-dark); font-weight: 500;
  }
  .dash-rule {
    position: absolute; left: 24px; right: 24px; top: 206px;
    border-top: 2px dotted var(--rule-grey);
  }
  .back-footer {
    position: absolute; left: 40px; top: 232px;
    font-family: "Oswald", "Arial Narrow", sans-serif;
    font-size: 14px; font-weight: 500; letter-spacing: 2px;
    color: var(--accent-red);
  }

  /* Front: brand side */
  .card--front {
    background: var(--card-black);
    display: flex; align-items: center; justify-content: center;
  }
  .front-pattern {
    position: absolute; inset: 0;
    background: radial-gradient(circle at 50% 45%, var(--pattern-tone), var(--card-black) 80%);
  }
  .card--front .brand-block { position: relative; margin-top: -10px; }
  .card--front .brand-name { font-size: 84px; color: var(--accent-red); }
  .card--front .brand-tagline {
    font-size: 13px; margin-top: 14px; color: var(--text-light);
  }
</style>
</head>
<body>
  <main class="stage">
    <section class="card card--back" aria-label="Card back with contact details">
      <div class="brand-block">
        <div class="brand-name">v-lumen</div>
        <div class="brand-tagline">WOMEN'S APPAREL</div>
      </div>
      <ul class="contact-fields">
        <li>NAME:</li>
        <li>TEL:</li>
        <li>ADDRESS:</li>
        <li>EMAIL:</li>
      </ul>
      <div class="dash-rule"></div>
      <div class="back-footer">WOMEN'S JUNIOR CONTEMPORARY APPAREL</div>
    </section>

    <section class="card card--front" aria-label="Card front with brand name">
      <div class="front-pattern" role="img" aria-label="Subtle dark damask pattern covering the card"></div>
      <div class="brand-block">
        <div class="brand-name">v-lumen</div>
        <div class="brand-tagline">WOMEN'S APPAREL</div>
      </div>
    </section>
  </main>
</body>
</html>
```